Seniors Massage Care Business Needs a New Website

Hello,
We require a website to be designed and coded. The design and coding must be high quality. Our website host has requested files be in static HTML format if possible.

The business is a mobile massage service for seniors (elderly people). The designer should emphasise that the business is a mobile service

The website will only have 4 pages.

1. Home- very simple layout and minimal information
2. Massage Services- this houses all of the information about the different services etc.
3. Contact Us-
4. ホーム (this is the Japanese symbol for 'home')- All of the information on the home page (section 1) will be translated into Japanese and uploaded to the brief for the designers to insert.

There is no requirement for an online booking, just contact information. The words 'Make a Booking' can be used and should lead customers to the 'Contact Us' page.

I have attached the business logo in multiple formats for designers to use.

I will upload more content and images to use for the website by the end of this week.

Thank you. I look forward to working with the successful candidate.

Target Market(s)

People aged 50+ years

Industry/Entity Type

Massage Therapy

Coding

Coded - Design and coding required

Number of Pages Required

4 page

Font styles to use
Sans Serif

Colors
74cabd
abd036
9ccb3b
f6faec
ffffff

Requirements
Must have
• Copyright free images and photos that we have taken. Both are important.
• Simple and inviting design.
Nice to have
• Colours of the logo incorporated.
Should not have
• This business is not a massage shop, so no images of massage shops or day salons required.
• Not too much imagery as the design needs to be simple.

```html
<!DOCTYPE html>
<html lang="en">
<head>
<meta charset="utf-8">
<title>Contact Us – Silver Comfort Massage</title>
<link rel="stylesheet" href="https://fonts.googleapis.com/css2?family=Lato:wght@400;700&family=Marcellus&family=Noto+Sans+JP:wght@500&display=swap">
<style>
:root{
  --green:#9ccb3b;
  --green-light:#abd036;
  --teal:#74cabd;
  --bg:#f6f8ee;
  --white:#ffffff;
  --ink:#2b2b2b;
  --muted:#6b6b6b;
  --line:#c9cdbf;
}
*{box-sizing:border-box;margin:0;padding:0}
html,body{width:1068px;height:1200px;overflow:hidden}
body{background:var(--bg);font-family:"Lato",sans-serif;color:var(--ink);position:relative}
.abs{position:absolute}

/* header */
.brand{position:absolute;display:flex;flex-direction:column;align-items:center;gap:6px}
.brand-mark{width:34px;height:34px;border-radius:50%;background:var(--green)}
.brand-name{font-family:"Marcellus",serif;color:var(--green);font-size:22px;letter-spacing:.5px;white-space:nowrap}
.site-header .brand{left:60px;top:14px;width:246px}
.contact-strip{display:flex;align-items:center;gap:10px;font-size:12px;line-height:16px}
.contact-strip svg{flex:none}
.nav{display:flex;font-family:"Marcellus",serif;font-size:15px;letter-spacing:2px;color:var(--ink)}
.nav a{color:inherit;text-decoration:none;white-space:nowrap}
.nav a.active{color:var(--green)}
.nav .jp{font-family:"Noto Sans JP",sans-serif;letter-spacing:1px}
.header-nav{left:522px;top:80px;gap:0}
.header-nav a{position:absolute;top:0}

.banner{left:60px;top:120px;width:961px;height:218px;
  background:linear-gradient(90deg,#5f7a4a 0%,#d9d4c9 30%,#c9c2b6 55%,#e4dfd6 70%,#8aa4c2 100%);
  box-shadow:0 18px 16px -14px rgba(0,0,0,.35)}

/* section title */
.section-title{left:0;width:1068px;top:376px;text-align:center;font-family:"Marcellus",serif;font-size:27px;letter-spacing:2px}
.section-title span{color:var(--green)}
.title-rule{left:391px;top:419px;width:288px;border-top:1px dotted #888}
.title-rule::after{content:"";position:absolute;left:102px;top:-2px;width:83px;height:3px;background:var(--green)}

/* columns */
.col-title{font-size:27px;font-weight:400;top:449px;white-space:nowrap}
.field{position:absolute;left:57px;width:411px;height:41px;background:var(--white);border:1px solid var(--line);border-radius:2px;padding:12px 11px;font-size:13px;color:var(--muted)}
.field b{color:#d33;font-weight:400}
.field.message{height:130px;border-radius:4px}
.send-btn{left:61px;top:814px;width:144px;height:42px;background:var(--green);color:var(--white);border-radius:2px;font-family:"Marcellus",serif;font-size:16px;display:flex;align-items:center;justify-content:center;letter-spacing:.5px}
.divider{left:512px;top:450px;width:1px;height:420px;background:linear-gradient(#fff0,#dfe2d6 15%,#dfe2d6 85%,#fff0)}
.map{left:543px;top:507px;width:476px;height:180px;background:linear-gradient(135deg,#e6e8e3 0%,#eeefeb 60%,#e3e6df 100%);border:1px solid #bfc3b8}
.info-row{position:absolute;left:543px;display:flex;align-items:center;gap:12px}
.icon-circle{width:32px;height:32px;border:1px solid #555;border-radius:50%;display:flex;align-items:center;justify-content:center;flex:none}
.info-text{font-size:13px;line-height:17px}
.info-text strong{color:var(--green);font-weight:700;display:block}
.info-phone{font-size:15px;font-weight:700}

/* footer */
.site-footer .brand{left:0;width:1068px;top:920px}
.site-footer .brand-name{font-size:28px}
.footer-nav a{position:absolute;top:1073px}
.social{left:0;width:1068px;top:1124px;display:flex;justify-content:center;gap:6px}
.social span{width:20px;height:20px;border-radius:50%;background:var(--green)}
.social span:nth-child(2){background:var(--teal)}
.social span:nth-child(3){background:var(--green-light)}
.copyright{left:0;top:1158px;width:1068px;height:42px;background:var(--green);color:var(--white);font-size:13px;display:flex;align-items:center;justify-content:center}
</style>
</head>
<body>
<header class="site-header">
  <div class="brand">
    <span class="brand-mark"></span>
    <span class="brand-name">Silver Comfort Massage</span>
  </div>
  <div class="contact-strip abs" style="left:698px;top:20px">
    <svg width="30" height="36" viewBox="0 0 30 36" aria-hidden="true"><path d="M9 4c-4 3-6 9-3 17s9 12 13 12l3-5-5-4-3 2c-3-2-5-6-6-10l3-2-2-6z" fill="none" stroke="var(--green)" stroke-width="2"/></svg>
    <div>Call Us:<br>0400 318 275</div>
  </div>
  <div class="contact-strip abs" style="left:845px;top:20px">
    <svg width="32" height="34" viewBox="0 0 32 34" aria-hidden="true"><path d="M3 10l26-6-4 24-22 2z M3 10l14 10 12-16" fill="none" stroke="var(--green)" stroke-width="2" stroke-linejoin="round"/></svg>
    <div>Mail Us:<br>hello@silvercomfort.com</div>
  </div>
  <nav class="nav header-nav abs">
    <a class="active" style="left:0">HOME</a>
    <a style="left:98px">MASSAGE SERVICES</a>
    <a class="jp" style="left:293px">ホーム</a>
    <a style="left:399px">CONTACT US</a>
  </nav>
  <div class="banner abs" role="img" aria-label="Photo strip of a mobile massage therapist visiting senior clients at home"></div>
</header>

<main>
  <h1 class="section-title abs">CONTACT <span>US</span></h1>
  <div class="title-rule abs"></div>

  <section class="inquiry">
    <h2 class="col-title abs" style="left:57px">Quick Inquiry</h2>
    <div class="field" style="top:507px">Name <b>*</b></div>
    <div class="field" style="top:559px">Email <b>*</b></div>
    <div class="field" style="top:611px">Phone</div>
    <div class="field message" style="top:663px">Message <b>*</b></div>
    <div class="send-btn abs">SEND INQUIRY</div>
  </section>

  <div class="divider abs"></div>

  <section class="details">
    <h2 class="col-title abs" style="left:543px">Silver Comfort Massage</h2>
    <div class="map abs" role="img" aria-label="Map showing the business location"></div>
    <div class="info-row" style="top:716px">
      <span class="icon-circle"><svg width="14" height="18" viewBox="0 0 14 18"><path d="M7 1a6 6 0 0 0-6 6c0 4 6 10 6 10s6-6 6-10a6 6 0 0 0-6-6z" fill="none" stroke="var(--green)" stroke-width="2"/><circle cx="7" cy="7" r="2" fill="var(--green)"/></svg></span>
      <div class="info-text"><strong>Silver Comfort Massage</strong>123 Lorem ipsum dolor sit amet, consectetuer adipiscing elit,<br>sed diam nonummy nibh euismod tincidunt.</div>
    </div>
    <div class="info-row" style="top:774px">
      <span class="icon-circle"><svg width="16" height="16" viewBox="0 0 16 16"><path d="M3 1l3 4-2 2c1 2 3 4 5 5l2-2 4 3-2 3C7 16 0 9 0 4z" fill="var(--green)"/></svg></span>
      <span class="info-phone">0400 318 275</span>
    </div>
    <div class="info-row" style="top:818px">
      <span class="icon-circle"><svg width="16" height="12" viewBox="0 0 16 12"><rect width="16" height="12" rx="1" fill="var(--green)"/><path d="M1 1l7 6 7-6" fill="none" stroke="#fff" stroke-width="1.5"/></svg></span>
      <span class="info-text" style="font-size:14px">hello@silvercomfort.com</span>
    </div>
  </section>
</main>

<footer class="site-footer">
  <div class="brand">
    <span class="brand-mark" style="width:44px;height:44px"></span>
    <span class="brand-name">Silver Comfort Massage</span>
  </div>
  <nav class="nav footer-nav">
    <a class="active" style="left:284px">HOME</a>
    <a style="left:382px">MASSAGE SERVICES</a>
    <a class="jp" style="left:578px">ホーム</a>
    <a style="left:684px">CONTACT US</a>
  </nav>
  <div class="social abs" aria-label="Social links"><span></span><span></span><span></span></div>
  <div class="copyright abs">Copyright © 2017 Silvercomfortmassage. All Right Reserved.</div>
</footer>
</body>
</html>
```